KerrLow Farm

Need a nice simple clean double sided business card that has our logo and info on:
Kerr Low Farm
Martin & Felicity Kerr Low
kerrlowfarm@mailbarn.example
Martin: 1-780-555-0148
Felicity: 1-780-555-0193
Instagram @ kerrlow_farm

Contact Information for Business Card

Martin & Felicity Kerr Low kerrlowfarm@mailbarn.example Martin: 1-780-555-0148 Felicity: 1-780-555-0193

```html
<!DOCTYPE html>
<html lang="en">
<head>
<meta charset="utf-8">
<title>Kerr Low Farm — Business Card</title>
<link rel="stylesheet" href="https://fonts.googleapis.com/css2?family=Cinzel:wght@400;700&family=Montserrat:wght@400&family=Arimo:wght@400&display=swap">
<style>
  :root {
    --backdrop: #c9c9c9;
    --leaf-green: #679f12;
    --deep-green: #5c9410;
    --harvest-orange: #f39c12;
    --ink: #3a3a3a;
    --paper: #ffffff;
    --mist: rgba(255,255,255,0.10);
    --mist-grey: rgba(0,0,0,0.045);
  }
  * { box-sizing: border-box; margin: 0; padding: 0; }
  html, body { width: 1200px; height: 900px; overflow: hidden; }
  body {
    background: var(--backdrop);
    display: flex;
    flex-direction: column;
    align-items: center;
    justify-content: center;
    gap: 60px;
  }
  .card {
    position: relative;
    width: 600px;
    height: 343px;
    border-radius: 30px;
    overflow: hidden;
    box-shadow: 0 6px 14px rgba(0,0,0,0.25);
  }
  .card-front { background: var(--leaf-green); }
  .card-back { background: var(--paper); }

  .wheat-decoration {
    position: absolute;
    right: -40px;
    top: -30px;
    width: 300px;
    height: 340px;
    border-radius: 50%;
  }
  .card-front .wheat-decoration { background: radial-gradient(ellipse at center, var(--mist), transparent 70%); }
  .card-back .wheat-decoration { background: radial-gradient(ellipse at center, var(--mist-grey), transparent 70%); }

  .brand {
    position: absolute;
    display: flex;
    flex-direction: column;
    align-items: center;
  }
  .brand-name-row { display: flex; align-items: center; gap: 14px; }
  .brand-mark {
    width: 44px; height: 44px;
    border-radius: 50%;
    border: 3px solid currentColor;
  }
  .brand-name {
    font-family: "Cinzel", serif;
    font-weight: 400;
    letter-spacing: 1px;
  }
  .tagline {
    font-family: "Montserrat", sans-serif;
    font-weight: 400;
    text-transform: uppercase;
  }

  .card-front .brand { left: 0; right: 0; top: 120px; color: var(--paper); }
  .card-front .brand-name { font-size: 44px; }
  .card-front .tagline { font-size: 15px; letter-spacing: 9px; margin-top: 6px; }

  .card-back .brand { left: 40px; top: 62px; align-items: flex-start; color: var(--deep-green); }
  .card-back .brand-name { font-size: 38px; }
  .card-back .tagline { font-size: 13px; letter-spacing: 8px; color: var(--harvest-orange); margin-top: 4px; }

  .owners {
    position: absolute;
    left: 40px; top: 180px;
    font-family: "Cinzel", serif;
    font-weight: 700;
    font-size: 17px;
    color: var(--deep-green);
  }
  .phone-list {
    position: absolute;
    left: 40px; top: 218px;
    list-style: none;
    display: flex; flex-direction: column; gap: 10px;
  }
  .contact-line {
    display: flex; align-items: center; gap: 10px;
    font-family: "Arimo", sans-serif;
    font-size: 17px;
    color: var(--ink);
  }
  .contact-label { color: var(--harvest-orange); }
  .icon { width: 24px; height: 24px; flex: none; }
  .online-list {
    position: absolute;
    right: 36px; top: 218px;
    list-style: none;
    display: flex; flex-direction: column; align-items: flex-end; gap: 10px;
  }
  .online-list .contact-line { flex-direction: row; }
</style>
</head>
<body>
  <section class="card card-front" aria-label="Card front">
    <div class="wheat-decoration" role="img" aria-label="Faint wheat stalk decoration"></div>
    <div class="brand">
      <div class="brand-name-row">
        <span class="brand-mark"></span>
        <span class="brand-name">KERR LOW FARM</span>
      </div>
      <span class="tagline">Stone Milled Flour</span>
    </div>
  </section>

  <section class="card card-back" aria-label="Card back">
    <div class="wheat-decoration" role="img" aria-label="Faint wheat stalk decoration"></div>
    <div class="brand">
      <div class="brand-name-row">
        <span class="brand-mark"></span>
        <span class="brand-name">KERR LOW FARM</span>
      </div>
      <span class="tagline">Stone Milled Flour</span>
    </div>
    <p class="owners">MARTIN &amp; FELICITY KERR LOW</p>
    <ul class="phone-list">
      <li class="contact-line">
        <svg class="icon" viewBox="0 0 24 24" aria-hidden="true"><circle cx="12" cy="12" r="10.5" fill="none" stroke="var(--leaf-green)" stroke-width="2"/><path d="M8.5 7.5c-1 1-1 3 1.5 5.5s4.5 2.5 5.5 1.5l-1.6-1.6-1.2.8c-.8-.4-2-1.6-2.4-2.4l.8-1.2z" fill="var(--leaf-green)"/></svg>
        <span><span class="contact-label">Martin:</span> 1-780-555-0148</span>
      </li>
      <li class="contact-line">
        <svg class="icon" viewBox="0 0 24 24" aria-hidden="true"><circle cx="12" cy="12" r="10.5" fill="none" stroke="var(--leaf-green)" stroke-width="2"/><path d="M8.5 7.5c-1 1-1 3 1.5 5.5s4.5 2.5 5.5 1.5l-1.6-1.6-1.2.8c-.8-.4-2-1.6-2.4-2.4l.8-1.2z" fill="var(--leaf-green)"/></svg>
        <span><span class="contact-label">Felicity:</span> 1-780-555-0193</span>
      </li>
    </ul>
    <ul class="online-list">
      <li class="contact-line">
        <span>kerrlowfarm@mailbarn.example</span>
        <svg class="icon" viewBox="0 0 24 24" aria-hidden="true"><circle cx="12" cy="12" r="10.5" fill="none" stroke="var(--leaf-green)" stroke-width="2"/><rect x="6.5" y="8" width="11" height="8" fill="var(--leaf-green)"/><path d="M6.5 8l5.5 4.5L17.5 8" fill="none" stroke="#fff" stroke-width="1.2"/></svg>
      </li>
      <li class="contact-line">
        <span>@ kerrlow_farm</span>
        <svg class="icon" viewBox="0 0 24 24" aria-hidden="true"><circle cx="12" cy="12" r="10.5" fill="none" stroke="var(--leaf-green)" stroke-width="2"/></svg>
      </li>
    </ul>
  </section>
</body>
</html>
```